Psychology service brochure

Marketing brochure for a new psychological counselling service.
Our old brochure was too boring and conservative. We are selling our services to GP's, psychiatrists, other health providers and of course potential clients. We'd really like a professional, elegant look that conveys us to be compassionate and conscientious providers of psychological services.
I have included a copy of our old brochure and a copy of the changes we'd like to the text.
Updates
I have included a photo of myself and my business partner. Only the faces are needed, so backgrounds would need to be edited out.
Hello, in consultation with my business partner, we would like
the use of our photos in the brochure please (with backgrounds edited out)
no stock photos of random people
use of abstract or nature/floral motifs suggestive of tranquillity
regards,
Miriam
Target Market(s)
General practitioner doctors, potential clients
Industry/Entity Type
Health
Requirements
Must have
- must include BlairMdITC TT- font for the business name
- must include our signature color Pantone 291 (see attached brochure)
- use of the photos of myself and my business partner (with background edited out please)
- keep use of colours to a minimum, 3 colors maximum, one of which must be Pantone 291
- must include changes to the brochure as outlined in the 'Changes to Pamphlet' document.
Nice to have
- an interesting, eye catching layout.
- interesting use of white spaces
- use of subtle abstract or nature/floral related graphics suggestive of tranquillity
Should not have
- should not include our fee
- stock photos of people

```html
<!DOCTYPE html>
<html lang="en">
<head>
<meta charset="utf-8">
<title>Quiet Harbour Counselling – Brochure</title>
<link rel="stylesheet" href="https://fonts.googleapis.com/css2?family=Arimo:wght@400;700&family=Michroma&display=swap">
<style>
  :root {
    --sky: #b4ecf0;
    --sky-deep: #8fdde6;
    --ink: #2e8a62;
    --white: #ffffff;
    --page: #f1f4f4;
    --paper: #ffffff;
    --fold: #e3eeee;
  }
  * { box-sizing: border-box; margin: 0; padding: 0; }
  html, body { width: 1200px; height: 900px; overflow: hidden; }
  body {
    background: var(--page);
    font-family: "Arimo", Arial, sans-serif;
    color: var(--ink);
    position: relative;
  }
  .spread {
    position: absolute;
    top: 130px;
    width: 540px;
    height: 640px;
    background: var(--paper);
    box-shadow: 0 6px 18px rgba(0,0,0,.12);
    display: flex;
  }
  .spread--outside { left: 45px; }
  .spread--inside { left: 615px; }
  .panel {
    position: relative;
    width: 180px;
    height: 100%;
    border-right: 1px solid var(--fold);
  }
  .panel:last-child { border-right: 0; }

  .section-band {
    background: var(--sky);
    color: var(--white);
    font-weight: 700;
    font-size: 11px;
    letter-spacing: .06em;
    text-transform: uppercase;
    line-height: 1.3;
    padding: 9px 14px;
    margin: 0 0 12px 0;
  }
  .body-copy {
    font-size: 9.5px;
    line-height: 1.38;
    padding: 0 14px;
  }
  .body-copy p { margin-bottom: 8px; }
  .benefit-list { list-style: none; }
  .benefit-list li {
    position: relative;
    padding-left: 10px;
    margin-bottom: 6px;
  }
  .benefit-list li::before {
    content: "";
    position: absolute;
    left: 0; top: 4px;
    width: 4px; height: 4px;
    background: var(--ink);
  }

  /* outside: left panel */
  .panel--approach { padding-top: 40px; border-left: 8px solid var(--sky); }
  .panel--approach .section-band { margin-left: -8px; }
  .panel--approach .section-band + .body-copy { margin-bottom: 10px; }

  /* outside: middle panel */
  .location-map {
    position: absolute;
    left: 16px; top: 150px;
    width: 148px; height: 190px;
    border-radius: 10px;
    border: 1px solid var(--sky-deep);
    background: linear-gradient(160deg, #f4fbf8, #dff3ec);
  }
  .contact-block {
    position: absolute;
    left: 0; right: 0; bottom: 70px;
    height: 170px;
    background: var(--sky);
    color: var(--white);
    font-size: 9.5px;
    font-style: normal;
    line-height: 1.6;
    padding: 16px 14px;
    text-align: center;
  }
  .contact-block .centre-name { font-weight: 700; letter-spacing: .05em; text-transform: uppercase; }
  .contact-block dl { display: grid; grid-template-columns: 34px 1fr; text-align: left; margin-top: 6px; }
  .contact-block dd { font-weight: 700; }

  /* outside: cover */
  .panel--cover {
    background: linear-gradient(200deg, #c6f1f4 0%, var(--sky) 45%, #9fe3ea 100%);
  }
  .cover-sky { position: absolute; inset: 0; }
  .brand-vertical {
    position: absolute;
    right: 14px; top: 24px;
    writing-mode: vertical-rl;
    font-family: "Michroma", sans-serif;
    font-size: 16px;
    font-weight: 400;
    letter-spacing: .08em;
    color: var(--white);
    white-space: nowrap;
  }

  /* inside: profiles */
  .panel--profiles { border-left: 8px solid var(--sky); }
  .profile-head {
    position: absolute;
    left: -8px; width: 188px;
    height: 78px;
  }
  .profile-head--first { top: 40px; }
  .profile-head--second { top: 308px; }
  .profile-photo {
    position: absolute;
    left: 14px; top: 8px;
    width: 52px; height: 62px;
    border-radius: 50%;
    background: radial-gradient(circle at 50% 40%, #e9dcd0, #c9b7a8);
  }
  .profile-title {
    position: absolute;
    left: 72px; right: 0; top: 0;
    background: var(--sky);
    color: var(--white);
    font-size: 8.5px;
    font-weight: 700;
    line-height: 1.35;
    padding: 9px 8px;
  }
  .profile-copy {
    position: absolute;
    left: 0; right: 0;
    font-size: 8px;
    line-height: 1.28;
    padding: 0 12px;
  }
  .profile-copy p { margin-bottom: 6px; }
  .profile-copy--first { top: 124px; }
  .profile-copy--second { top: 392px; }

  .profile-rule {
    position: absolute;
    left: 0; width: 180px;
    height: 3px;
    background: var(--sky);
  }
  .profile-rule--first { top: 60px; }
  .profile-rule--second { top: 328px; }
  .profile-continued { position: absolute; left: 0; right: 0; }
  .profile-continued--first { top: 74px; }
  .profile-continued--second { top: 342px; }

  .brand-footer {
    position: absolute;
    left: 6px; bottom: 16px;
    width: 340px;
    font-family: "Michroma", sans-serif;
    font-size: 15.5px;
    letter-spacing: .06em;
    color: var(--sky-deep);
    white-space: nowrap;
    z-index: 1;
  }

  /* inside: fees */
  .panel--fees { padding-top: 46px; border-top: 10px solid var(--sky); }
  .panel--fees .section-band { margin-left: 14px; }
  .fee-note {
    position: absolute;
    left: 0; right: 0; bottom: 70px;
    height: 110px;
    background: var(--sky);
    color: var(--white);
    font-size: 9px;
    line-height: 1.4;
    padding: 16px 14px;
  }
</style>
</head>
<body>

<section class="spread spread--outside" aria-label="Brochure outside">
  <article class="panel panel--approach">
    <h2 class="section-band">Our approach to therapy</h2>
    <div class="body-copy">
      <p>We are warm, compassionate and professional Clinical and General Psychologists who together have thirty years of experience and who are committed to providing high quality, evidence-based treatment to our clients.</p>
      <p>Types of treatment may include Cognitive Behavioural Therapy, Motivational Interviewing and Mindfulness.</p>
      <p>We are also eligible to provide Pregnancy Support Counselling services under Medicare.</p>
    </div>
    <h2 class="section-band">What we want for our clients</h2>
    <ul class="body-copy benefit-list">
      <li>For you to feel heard and respected</li>
      <li>To have a positive experience of working collaboratively with a psychologist</li>
      <li>To connect or reconnect with feelings of hope</li>
      <li>To move beyond counselling with an understanding of your strengths and the skills to make changes that will help you to meet future challenges.</li>
    </ul>
  </article>

  <article class="panel panel--contact">
    <div class="location-map" role="img" aria-label="Street map showing the practice location near the station"></div>
    <address class="contact-block">
      <div>Contact reception</div>
      <div class="centre-name">The Linwood Centre</div>
      <div>18 Linwood Street, Fairvale 3071</div>
      <dl>
        <dt>Phone</dt><dd>9317 2046</dd>
        <dt>Fax</dt><dd>9317 2047</dd>
        <dt>Email</dt><dd>hello@quietharbour.net</dd>
      </dl>
    </address>
  </article>

  <article class="panel panel--cover">
    <div class="cover-sky" role="img" aria-label="Soft sky with drifting white clouds"></div>
    <h1 class="brand-vertical">Quiet Harbour Counselling</h1>
  </article>
</section>

<section class="spread spread--inside" aria-label="Brochure inside">
  <article class="panel panel--profiles">
    <div class="profile-head profile-head--first">
      <div class="profile-photo" role="img" aria-label="Portrait of Miriam Ashdown"></div>
      <div class="profile-title">Miriam Ashdown<br>Clinical Psychologist<br>M Psych (Clin) | MAPS</div>
    </div>
    <div class="profile-copy profile-copy--first">
      <p>Miriam is a Clinical Psychologist with fifteen years of experience providing a range of psychological services to challenging clients within the public mental health sector including forensic, addiction and dual diagnosis services. She has been employed as a Senior Psychologist in this capacity for the last seven years.</p>
      <p>Miriam is a trained and experienced Cognitive Behavioural Therapist and is skilled in treating individuals and groups with a range of mood disorders including anxiety, depression and panic disorder,</p>
    </div>

    <div class="profile-head profile-head--second">
      <div class="profile-photo" role="img" aria-label="Portrait of Helena Marsh"></div>
      <div class="profile-title">Helena Marsh<br>Psychologist<br>M Psych (Clin) | MAPS</div>
    </div>
    <div class="profile-copy profile-copy--second">
      <p>Helena is a Psychologist, and with fifteen years experience working in the public health sector, seven as a Senior Psychologist, she is a highly skilled clinician in the areas of mental health, addiction and dual diagnosis.</p>
      <p>She has more recently specialised in working with adolescents but has significant experience treating adults, both individually and in a variety of group programmes. She has also facilitated numerous training events and mentored clinicians in addressing dual diagnosis issues with their clients.</p>
    </div>

    <div class="brand-footer">Quiet Harbour Counselling</div>
  </article>

  <article class="panel panel--profiles-continued">
    <div class="profile-rule profile-rule--first"></div>
    <div class="profile-continued profile-continued--first body-copy">
      <p>as well as in helping clients to overcome life issues such as grief and loss, stress management and anger management.</p>
      <p>Miriam trains other mental health clinicians and university students in treatment modalities including Motivational Interviewing and Brief Interventions. She has an interest in brain-based research into neuroplasticity and it's application to cognitive therapy and change.</p>
    </div>
    <div class="profile-rule profile-rule--second"></div>
    <div class="profile-continued profile-continued--second body-copy">
      <p>Helena primarily utilises a Cognitive Behavioural framework and Motivational Interviewing and has a special interest in working with adolescents who are experiencing developmental difficulties, antenatal and post-natal depression/stress, and parenting issues. Additionally Helena is skilful working in the areas of grief &amp; loss, life transition and adjustment issues, relationship and interpersonal challenges, and personal development.</p>
    </div>
  </article>

  <article class="panel panel--fees">
    <h2 class="section-band">Our fee structure</h2>
    <div class="body-copy">
      <p>The practice accepts referrals from self-referring individuals, as well as from health professionals such as GPs, Psychiatrists, and Maternal and Child Health Nurses.</p>
      <p>Medicare rebates are available for clients referred for treatment by their GP.</p>
      <p>There are different tiers of rebates for Psychologists under Medicare, and this is dependent on treatment received (individual, group or pregnancy support counselling), and whether you are treated by a Psychologist or a Clinical Psychologist.</p>
      <p>Please contact us directly to further discuss fees for treatment.</p>
      <p>Fees are paid in full at the end of each session, and a receipt is provided which will allow you to obtain your refund at any Medicare office.</p>
    </div>
    <p class="fee-note">The practice does not bulk bill at this time, but we anticipate the addition of this facility in the future.</p>
  </article>
</section>

</body>
</html>
```